FurryAsk.net Skin

I need a header image, backgroundand partial colour scheme for our website furryask.net.

We use a cms so have very limited ability to change the design.

We can change: link / button colour, header size and image, background image.
See these examples: http://replies.mockupvista.org/ and http://aid.zelwick.org/

Target Market(s)

Pet owners are the audience, probably slightly more females than males.

Number of Pages Required

1 page

Requirements
Nice to have
• Should be friendly and fun with an "organic" feel. Can contain images of pets but it isn"t a requirement.

```html
<!DOCTYPE html>
<html lang="en">
<head>
<meta charset="utf-8">
<title>FurryAsk.net – Pet Q&amp;A Community</title>
<link rel="stylesheet" href="https://fonts.googleapis.com/css2?family=Arimo:wght@400;700&family=Yanone+Kaffeesatz:wght@400;600&display=swap">
<style>
:root{
  --bg:#2f251a;
  --cream:#fbf8e6;
  --cream-dark:#e3e0c6;
  --orange:#fcb23a;
  --orange-dark:#f39a1c;
  --orange-text:#f08a00;
  --teal:#0e8f8c;
  --teal-dark:#06706d;
  --teal-light:#1cb7b3;
  --ink:#1a1a1a;
  --bar:#151515;
  --white:#ffffff;
  --grey:#999a8c;
}
*{box-sizing:border-box;margin:0;padding:0}
html,body{width:859px;height:1200px;overflow:hidden}
body{background:var(--bg);font-family:"Arimo",Arial,sans-serif;color:var(--ink);position:relative}
.abs{position:absolute}
h1,h2,h3{font-weight:400}

/* header */
.site-header{left:43px;top:21px;width:773px;height:89px;border-radius:45px;background:linear-gradient(#fbfaf0,var(--cream-dark));z-index:3}
.brand{left:48px;top:20px}
.brand-name{font-size:30px;font-weight:700;color:var(--orange-text);display:flex;align-items:center;gap:8px;letter-spacing:-.5px}
.brand-dot{width:22px;height:22px;border-radius:50%;background:var(--orange)}
.brand-tag{font-size:10px;font-weight:700;color:#333;margin-top:2px}
.account{left:567px;top:22px;width:140px;height:18px;border-radius:9px;background:linear-gradient(#ffc766,var(--orange-dark));color:var(--white);font-size:11px;font-weight:700;display:flex;justify-content:center;align-items:center;gap:8px}
.main-nav{left:437px;top:50px;font-size:11px;font-weight:700;display:flex;gap:12px}
.main-nav span.sep{color:#333}

/* welcome */
.welcome-frame{left:84px;top:86px;width:692px;height:204px;background:linear-gradient(var(--orange),var(--orange-dark));border-radius:0 0 58px 58px;z-index:2}
.welcome-inner{left:26px;top:24px;width:640px;height:138px;background:linear-gradient(var(--white) 45%,#fde3ad);border-radius:0 0 30px 30px}
.welcome-title{left:30px;top:8px;font-family:"Yanone Kaffeesatz",sans-serif;font-size:30px;width:440px;border-bottom:1px solid var(--orange-dark);padding-bottom:1px}
.welcome-text{left:30px;top:50px;width:410px;font-size:11.5px;line-height:15.5px;color:#333}
.welcome-text b{color:var(--teal-dark)}
.members{left:535px;top:34px;width:120px;height:108px;border-radius:18px;background:var(--teal);border:3px solid var(--white);box-shadow:0 0 0 2px var(--teal-dark);color:var(--white);text-align:center;font-weight:700}
.members .count{font-size:50px;line-height:56px;margin-top:10px}
.members .label{font-size:19px}
.search-bar{left:42px;top:154px;width:610px;height:46px;border-radius:23px;background:linear-gradient(#fde7b8,#fcc55a);display:flex;align-items:center;padding-left:14px;gap:10px}
.search-label{font-family:"Yanone Kaffeesatz",sans-serif;font-weight:600;font-size:21px}
.search-field{width:234px;height:22px;border-radius:11px;background:var(--white)}
.join{font-size:20px;font-weight:700;color:var(--teal-dark);margin-left:4px;text-shadow:0 0 2px var(--white),0 0 2px var(--white)}

/* main panel */
.main-panel{left:47px;top:302px;width:771px;height:846px;border-radius:58px;background:var(--white);border:2px solid #d8d4c0}
.box-head{height:25px;font-size:18px;padding-left:8px;line-height:25px;border:1px solid #d4cfb3;font-weight:400}
.ask-head{left:36px;top:21px;width:455px;background:linear-gradient(#ffc862,var(--orange-dark))}
.ask-area{left:36px;top:53px;width:455px;height:188px;border:1px solid #d4d2c4;box-shadow:inset 0 0 4px #e5e3d6}
.tag-btn{left:36px;top:249px;width:135px;height:26px;background:var(--teal);color:var(--white);font-size:12px;display:flex;align-items:center;gap:6px;padding-left:8px}
.ask-btn{left:366px;top:249px;width:125px;height:26px;background:linear-gradient(#ffc862,var(--orange-dark));color:var(--white);font-size:17px;text-align:center;line-height:26px}
.latest-head{left:36px;top:284px;width:455px;background:linear-gradient(var(--white),var(--cream-dark));display:flex;justify-content:space-between;padding-right:8px}
.latest-tabs{font-size:11px;font-weight:700;display:flex;gap:10px}
.latest-tabs .active{color:var(--teal-dark)}

.questions{left:36px;top:324px;width:455px}
.question{height:90px;position:relative}
.q-avatar{position:absolute;left:0;top:3px;width:39px;height:39px;border:1px solid #888}
.q-text{position:absolute;left:44px;top:0;width:408px;font-size:12px;line-height:15.5px}
.q-bar{position:absolute;left:0;top:59px;width:455px;height:17px;display:flex;font-size:11px}
.q-meta{flex:1;background:var(--bar);color:var(--white);display:flex;justify-content:space-between;align-items:center;padding:0 7px;font-size:10px}
.q-meta b{color:var(--teal-light);font-size:11px}
.q-meta .topic{font-weight:700;font-size:11px}
.q-answer{width:73px;margin-left:2px;background:var(--teal);color:var(--orange);font-weight:700;text-align:center;line-height:17px}
.q-answer span{color:#dff}

.pager{left:36px;top:791px;width:455px;height:29px;border:1px solid #d4cfb3;background:linear-gradient(var(--cream),var(--white));display:flex;align-items:center;justify-content:center;gap:6px;font-size:11px;font-weight:700}
.pager .pg-btn{background:linear-gradient(#ffc862,var(--orange-dark));border:1px solid #c77a00;padding:1px 5px}

/* sidebar */
.sidebar{left:508px;top:21px;width:223px;height:800px;background:var(--cream);border:1px solid #dcd8bd;overflow:hidden;border-radius:0 0 40px 40px}
.side-title{left:8px;font-size:18px;font-weight:400}
.active-card{left:7px;width:210px;height:60px;background:linear-gradient(var(--teal-light),var(--teal));border:1px solid var(--teal-dark);color:var(--white);font-weight:700;font-size:11.5px}
.active-card .avatar{position:absolute;left:11px;top:10px;width:39px;height:39px;border:1px solid var(--white)}
.active-card .name{position:absolute;left:59px;top:14px}
.active-card .stat{position:absolute;left:59px;top:35px;width:140px;display:flex;justify-content:space-between}
.tag{left:7px;height:20px;background:var(--white);border:1px solid #d8d6cc;color:var(--grey);font-size:11.5px;display:flex;justify-content:space-between;align-items:center;padding:0 6px}
.side-promo{left:0;bottom:0;width:223px;height:48px;background:var(--bar);display:flex;align-items:center;justify-content:space-between;padding:0 22px 0 18px}
.promo-brand{color:var(--orange);font-size:14px;font-weight:700}
.promo-cta{color:var(--orange);font-weight:700;font-size:14px;text-align:center;line-height:15px}

.site-footer{left:0;top:1158px;width:859px;text-align:center;color:var(--white);font-size:10px;font-weight:700}
</style>
</head>
<body>

<header class="site-header abs">
  <div class="brand abs">
    <div class="brand-name">furryask <span class="brand-dot"></span></div>
    <div class="brand-tag">the best website for our best friends</div>
  </div>
  <div class="account abs"><span>Sign In</span><span>|</span><span>Sign Up</span></div>
  <nav class="main-nav abs">
    <span>Home</span><span class="sep">|</span><span>Help</span><span class="sep">|</span><span>Terms</span><span class="sep">|</span><span>Privacy</span><span class="sep">|</span><span>Contact</span>
  </nav>
</header>

<section class="welcome-frame abs">
  <div class="welcome-inner abs">
    <h1 class="welcome-title abs">Welcome</h1>
    <p class="welcome-text abs"><b>FurryAsk.net</b> is <b>Q&amp;A community</b> dedicated to helping pet owners all over the world.<br>Got a problem pooch or trouble with a tortoise? Get free answers from the FurryAsk.net community.</p>
    <div class="members abs"><div class="count">270</div><div class="label">MEMBERS</div></div>
  </div>
  <div class="search-bar abs">
    <span class="search-label">Search</span>
    <span class="search-field"></span>
    <svg width="26" height="26" viewBox="0 0 26 26"><circle cx="10" cy="10" r="7" fill="#dff3ff" stroke="#7a9fb5" stroke-width="2.5"/><line x1="15" y1="15" x2="23" y2="23" stroke="#b07a2a" stroke-width="4" stroke-linecap="round"/></svg>
    <span class="join">JOIN or ASK QUESTION</span>
  </div>
</section>

<main class="main-panel abs">
  <h2 class="box-head ask-head abs">Ask A Question</h2>
  <div class="ask-area abs"></div>
  <div class="tag-btn abs">
    <svg width="18" height="16" viewBox="0 0 18 16"><path d="M2 8 L7 13 L16 2" fill="none" stroke="#f5a623" stroke-width="3.5" stroke-linecap="round"/></svg>
    Tag This Question
  </div>
  <div class="ask-btn abs">Ask Question</div>

  <div class="box-head latest-head abs">
    <span>Latest Question</span>
    <span class="latest-tabs"><span class="active">Questions</span>|<span>Popular</span>|<span>Activity</span></span>
  </div>

  <div class="questions abs">
    <article class="question">
      <div class="q-avatar" role="img" aria-label="Member photo of a dog" style="background:linear-gradient(#8a6a48,#3a2a1c)"></div>
      <p class="q-text">Our Brittney is just 3 Yrs old, latley when we leave home he tears up his bed and other things in his room. We leave a radio on but it dose'nt help. What can we try to do?</p>
      <div class="q-bar"><div class="q-meta"><span>asked by <b>Ray Marlow</b></span><span class="topic">dog behavior</span></div><div class="q-answer">answer <span>| 1</span></div></div>
    </article>
    <article class="question">
      <div class="q-avatar" role="img" aria-label="Member photo of a dog on grass" style="background:linear-gradient(#b9c98a,#6c8a3c)"></div>
      <p class="q-text">My Dog recently started getting goopy eyes? What can I do?</p>
      <div class="q-bar"><div class="q-meta"><span>asked by <b>Lacey</b></span><span class="topic">goopy wyes</span></div><div class="q-answer">answer <span>| 1</span></div></div>
    </article>
    <article class="question">
      <div class="q-avatar" role="img" aria-label="Member photo of a kitten" style="background:linear-gradient(#c9c4bc,#7d746a)"></div>
      <p class="q-text">What vegetables can I feed my dog?</p>
      <div class="q-bar"><div class="q-meta"><span>asked by <b>Ray Marlow</b></span><span class="topic">dog food</span></div><div class="q-answer">answer <span>| 1</span></div></div>
    </article>
    <article class="question">
      <div class="q-avatar" role="img" aria-label="Member photo of a small terrier" style="background:linear-gradient(#e9c79a,#b07a45)"></div>
      <p class="q-text">Our Brittney is just 3 Yrs old, latley when we leave home he tears up his bed and other things in his room. We leave a radio on but it dose'nt help. What can we try to do?</p>
      <div class="q-bar"><div class="q-meta"><span>asked by <b>Zelene</b></span><span class="topic">cat behavior</span></div><div class="q-answer">answer <span>| 1</span></div></div>
    </article>
    <article class="question">
      <div class="q-avatar" role="img" aria-label="Member photo of a cockatoo" style="background:linear-gradient(#fbf3d9,#e6b85c)"></div>
      <p class="q-text">My st.bernard feels fevered. Is it alright to give a small dose of baby fever drops?</p>
      <div class="q-bar"><div class="q-meta"><span>asked by <b>Nora Pell</b></span><span class="topic">dog fever</span></div><div class="q-answer">answer <span>| 1</span></div></div>
    </article>
  </div>

  <nav class="pager abs">
    <span class="pg-btn">&lt;&lt; Previous</span>
    <span>1</span>|<span>2</span>|<span>3</span>|<span>4</span>|<span>5</span>|<span>6</span>|<span>7</span>|<span>8</span>|<span>9</span><span>…</span><span>244</span>
    <span class="pg-btn">Next &gt;&gt;</span>
  </nav>

  <aside class="sidebar abs">
    <h3 class="side-title abs" style="top:6px">Most Active</h3>
    <div class="active-card abs" style="top:31px">
      <div class="avatar" role="img" aria-label="Phobe's dog photo" style="background:linear-gradient(#c6d59a,#7a9a4c)"></div>
      <span class="name">Phobe</span><span class="stat"><span>Answers</span><span>37</span></span>
    </div>
    <div class="active-card abs" style="top:97px">
      <div class="avatar" role="img" aria-label="Ledey's kitten photo" style="background:linear-gradient(#e8e8e8,#333)"></div>
      <span class="name">Ledey</span><span class="stat"><span>Answers</span><span>33</span></span>
    </div>
    <div class="active-card abs" style="top:163px">
      <div class="avatar" role="img" aria-label="Zelene's terrier photo" style="background:linear-gradient(#f2d3a8,#b57d46)"></div>
      <span class="name">Zelene</span><span class="stat"><span>Answers</span><span>27</span></span>
    </div>

    <h3 class="side-title abs" style="top:234px">Popular Tags</h3>
    <div class="tag abs" style="top:265px;width:209px"><span>health concern</span><span>238</span></div>
    <div class="tag abs" style="top:290px;width:197px"><span>weight</span><span>237</span></div>
    <div class="tag abs" style="top:315px;width:187px"><span>temperment</span><span>236</span></div>
    <div class="tag abs" style="top:340px;width:176px"><span>life Expectancy</span><span>234</span></div>
    <div class="tag abs" style="top:365px;width:168px"><span>Colors</span><span>230</span></div>

    <div class="side-promo abs">
      <span class="promo-brand">Zelwick</span>
      <span class="promo-cta">Create Your<br>Own Zelwick</span>
    </div>
  </aside>
</main>

<footer class="site-footer abs">© 2010, All Rights Reserved, www.furryask.net</footer>

</body>
</html>
```